STATIONARY PACK FOR LOADMARK
Business Cards, Email Footer, A4 Presentation Folder, Letterhead etc
Project: STATIONARY PACK FOR LOADMARK
STATIONARY PACK FOR LOADMARK - Construction
Creative Brief
Simple
Colin Bradshaw
General Manager
Level 3 248Harbour Road Auckland 1010
colin@loadmark.example.nz
www.loadmark.example.nz
Please ensure you make the following as part of this design package, Email footer, Business Card Double Sided, Letterhead, A4 Presentation folder.
loadmark.example.nz in the bottom left corner Solid Colour Matt Finish "Equipment hire made easy"

```html
<!DOCTYPE html>
<html lang="en">
<head>
<meta charset="utf-8">
<title>LOADMARK Business Card</title>
<link rel="stylesheet" href="https://fonts.googleapis.com/css2?family=Open+Sans:wght@400;600;700&display=swap">
<style>
  :root {
    --navy: #2c3350;
    --orange: #f06a35;
    --white: #ffffff;
    --backdrop: #e3e3e5;
    --ink-soft: #e8eaf2;
  }
  * { margin: 0; padding: 0; box-sizing: border-box; }
  html, body { width: 1200px; height: 902px; overflow: hidden; }
  body {
    background: var(--backdrop);
    font-family: "Open Sans", Arial, sans-serif;
    position: relative;
  }
  .card {
    position: absolute;
    left: 260px;
    width: 680px;
    height: 388px;
    background: var(--white);
    box-shadow: 0 6px 18px rgba(0,0,0,0.12);
    overflow: hidden;
  }
  .card--front { top: 43px; }
  .card--back { top: 471px; }

  .brand { position: absolute; }
  .brand__name {
    font-weight: 700;
    color: var(--navy);
    letter-spacing: 1px;
    line-height: 1;
  }
  .brand__tagline {
    color: var(--navy);
    font-weight: 400;
    margin-top: 6px;
    white-space: nowrap;
  }
  .card--front .brand {
    left: 0; right: 0; top: 150px; text-align: center;
  }
  .card--front .brand__name { font-size: 52px; }
  .card--front .brand__tagline { font-size: 17px; }

  .card--back .brand { left: 40px; top: 168px; }
  .card--back .brand__name { font-size: 40px; }
  .card--back .brand__tagline { font-size: 13px; }

  .back-shapes { position: absolute; inset: 0; }

  .contact {
    position: absolute;
    right: 36px;
    top: 46px;
    text-align: right;
    color: var(--white);
  }
  .contact__name { font-size: 20px; font-weight: 600; white-space: nowrap; }
  .contact__role { font-size: 16px; margin-bottom: 26px; color: var(--ink-soft); }
  .contact__line {
    font-size: 14px;
    line-height: 22px;
    display: flex;
    justify-content: flex-end;
    align-items: center;
    gap: 8px;
    white-space: nowrap;
  }
  .contact__line svg { width: 12px; height: 12px; fill: var(--white); flex: none; }
  .contact__spacer { width: 12px; flex: none; }
</style>
</head>
<body>

<section class="card card--front" aria-label="Business card front">
  <div class="brand">
    <div class="brand__name">LOADMARK</div>
    <div class="brand__tagline">Equipment hire made easy</div>
  </div>
</section>

<section class="card card--back" aria-label="Business card back">
  <svg class="back-shapes" viewBox="0 0 680 388" width="680" height="388" aria-hidden="true">
    <rect width="680" height="388" fill="var(--navy)"/>
    <path d="M0 0 H300 C420 110 410 290 330 388 H0 Z" fill="var(--orange)"/>
    <path d="M0 0 H270 C385 120 370 295 290 388 H0 Z" fill="var(--white)"/>
  </svg>

  <div class="brand">
    <div class="brand__name">LOADMARK</div>
    <div class="brand__tagline">Equipment hire made easy</div>
  </div>

  <div class="contact">
    <div class="contact__name">Colin Bradshaw</div>
    <div class="contact__role">Consultant</div>
    <div class="contact__line">Level 3 248Harbour Road<span class="contact__spacer"></span></div>
    <div class="contact__line">Auckland 1010
      <svg viewBox="0 0 24 24"><path d="M12 2a7 7 0 0 0-7 7c0 5 7 13 7 13s7-8 7-13a7 7 0 0 0-7-7zm0 9.5A2.5 2.5 0 1 1 12 6a2.5 2.5 0 0 1 0 5.5z"/></svg>
    </div>
    <div class="contact__line">021 555 0143
      <svg viewBox="0 0 24 24"><path d="M6.6 10.8a15 15 0 0 0 6.6 6.6l2.2-2.2a1 1 0 0 1 1-.25 11.4 11.4 0 0 0 3.6.57 1 1 0 0 1 1 1V20a1 1 0 0 1-1 1A17 17 0 0 1 3 4a1 1 0 0 1 1-1h3.5a1 1 0 0 1 1 1c0 1.250.2 2.45.57 3.57a1 1 0 0 1-.25 1z"/></svg>
    </div>
    <div class="contact__line">colin@loadmark.example.nz
      <svg viewBox="0 0 24 24"><path d="M2 5h20v14H2z M4 7v.5l8 5 8-5V7l-8 5z" fill-rule="evenodd"/></svg>
    </div>
    <div class="contact__line">www.loadmark.example.nz
      <svg viewBox="0 0 24 24"><path d="M12 2a10 10 0 1 0 0 20 10 10 0 0 0 0-20zm6.9 6h-3a15 15 0 0 0-1.3-3.9A8 8 0 0 1 18.9 8zM12 4c.8 1.1 1.5 2.5 1.9 4h-3.8c.4-1.5 1.1-2.900 1.9-4zM4.3 14a8 8 0 0 1 0-4h3.4a16 16 0 0 0 0 4zm.8 2h3a15 15 0 0 0 1.3 3.9A8 8 0 0 1 5.1 16zm3-8h-3a8 8 0 0 1 4.3-3.9A15 15 0 0 0 8.1 8zM12 20c-.8-1.1-1.5-2.5-1.9-4h3.8c-.4 1.5-1.1 2.9-1.9 4zm2.3-6H9.7a14 14 0 0 1 0-4h4.6a14 14 0 0 1 0 4zm.3 5.9a15 15 0 0 0 1.3-3.9h3a8 8 0 0 1-4.3 3.9zM16.3 14a16 16 0 0 0 0-4h3.4a8 8 0 0 1 0 4z"/></svg>
    </div>
  </div>
</section>

</body>
</html>
```